Business Card Design Project

Lorantte is a women fashion house focusing on youthful glamour.

We bring together unique designs, premium quality materials and top craftsmanship to deliver sophisticated yet playful glamour, fun and excitement to the confident woman.

We can sum up the brand identity in 3 words:
Glamour – Sophistication – Unique

Industry/Entity Type

Fashion

Requirements
Must have
• Nim Tressoli
nim.tressoli@lorantte-example.com
Mobile: 081 536 2947
Instragram: lorantte_label
Facebook: lorantte

Creative Director
Lorantte Co., LTD
TEL: 02 417 39 86
47 Mango Row, 2nd Floor , D Building , Thonburi Court , Soi Ratchada 29.
Upper Bangrak , Sathorn , Bangkok 10500 Thailand
www.lorantte-example.com

```html
<!DOCTYPE html>
<html lang="en">
<head>
<meta charset="utf-8">
<title>Lorantte Co., LTD – Business Card</title>
<link rel="stylesheet" href="https://fonts.googleapis.com/css2?family=PT+Serif:wght@400;700&display=swap">
<style>
  :root {
    --stage: #e8e5e0;
    --paper: #fbfbfa;
    --ink: #4b4b4b;
    --ink-soft: #707070;
    --ornament-light: #efefef;
    --back-top: #6e6e6e;
    --back-bottom: #1c1c1c;
    --back-ink: #f4f4f4;
    --band: #c9c9c9;
    --band-ink: #454545;
    --edge: #2a2a2a;
  }
  * { margin: 0; padding: 0; box-sizing: border-box; }
  html, body {
    width: 1200px; height: 1023px; overflow: hidden;
    background: var(--stage);
    font-family: "PT Serif", Georgia, serif;
  }
  .card {
    position: absolute; left: 220px; width: 760px; height: 440px;
    box-shadow: 0 10px 28px rgba(0,0,0,.22);
    overflow: hidden;
  }
  /* Front */
  .card--front { top: 44px; background: var(--paper); color: var(--ink); }
  .front__ornament {
    position: absolute; left: 180px; top: 0; width: 420px; height: 250px;
    background: radial-gradient(ellipse at center, var(--ornament-light) 0%, rgba(239,239,239,0) 70%);
  }
  .front__brand { position: absolute; right: 56px; top: 34px; text-align: right; }
  .brand-name { font-size: 66px; line-height: 1; font-weight: 400; letter-spacing: 1px; }
  .brand-suffix { font-size: 20px; margin-top: 4px; }
  .front__address {
    position: absolute; left: 420px; top: 200px;
    font-size: 17px; line-height: 1.5; display: flex; gap: 8px;
  }
  .front__address svg { flex: none; margin-top: 4px; }
  .front__person { position: absolute; left: 60px; top: 170px; }
  .person-name { font-size: 25px; letter-spacing: 2px; font-weight: 400; }
  .person-title { font-size: 16px; color: var(--ink-soft); margin-top: 2px; }
  .front__contacts { position: absolute; left: 92px; top: 252px; list-style: none; font-size: 15px; }
  .front__contacts li { display: flex; align-items: center; gap: 9px; height: 22px; }
  .front__contacts li.group-start { margin-top: 12px; }
  .front__contacts svg { flex: none; }

  /* Back */
  .card--back {
    top: 534px; color: var(--back-ink);
    background: linear-gradient(160deg, var(--back-top) 0%, #3a3a3a 45%, var(--back-bottom) 100%);
  }
  .back__gloss {
    position: absolute; inset: 0;
    background: linear-gradient(200deg, rgba(255,255,255,.18) 0%, rgba(255,255,255,0) 35%);
  }
  .back__ornament {
    position: absolute; left: 450px; top: 30px; width: 290px; height: 320px;
    background: radial-gradient(ellipse at center, rgba(150,150,150,.35) 0%, rgba(120,120,120,0) 70%);
  }
  .back__brand { position: absolute; left: 70px; top: 70px; }
  .back__brand .brand-name { font-size: 112px; }
  .back__brand .brand-suffix { font-size: 34px; text-align: right; margin-top: 6px; }
  .back__band {
    position: absolute; left: 0; right: 0; bottom: 44px; height: 48px;
    background: var(--band); color: var(--band-ink);
    font-size: 23px; line-height: 48px; padding-left: 26px;
  }
  .back__edge { position: absolute; left: 0; right: 0; bottom: 0; height: 44px; background: var(--edge); }
</style>
</head>
<body>

<section class="card card--front" aria-label="Business card front">
  <div class="front__ornament" role="img" aria-label="Faint floral flourish ornament"></div>

  <div class="front__brand">
    <div class="brand-name">Lorantte</div>
    <div class="brand-suffix">Co., LTD</div>
  </div>

  <address class="front__address" style="font-style:normal">
    <svg width="12" height="16" viewBox="0 0 12 16" aria-hidden="true"><path d="M6 0a6 6 0 0 1 6 6c0 4-6 10-6 10S0 10 0 6a6 6 0 0 1 6-6z" fill="#4b4b4b"/><circle cx="6" cy="6" r="2.2" fill="#fbfbfa"/></svg>
    <span>47 Mango Row, 2nd Floor ,<br>D Building , Thonburi Court ,<br>Soi Ratchada 29.<br>Upper Bangrak , Sathorn ,<br>Bangkok 10500 Thailand</span>
  </address>

  <div class="front__person">
    <div class="person-name">NIM TRESSOLI</div>
    <div class="person-title">Creative Director</div>
  </div>

  <ul class="front__contacts">
    <li><svg width="14" height="14" viewBox="0 0 14 14" aria-hidden="true"><path d="M3 1l2 3-1.3 1.3a8 8 0 0 0 5 5L10 9l3 2-1.5 2.5C6 13 1 8 .5 2.5z" fill="#4b4b4b"/></svg>02 417 39 86</li>
    <li><svg width="14" height="14" viewBox="0 0 14 14" aria-hidden="true"><rect x="3.5" y="0.5" width="7" height="13" rx="1.5" fill="#4b4b4b"/><rect x="5" y="2" width="4" height="8" fill="#fbfbfa"/></svg>081 536 2947</li>
    <li class="group-start"><svg width="14" height="14" viewBox="0 0 14 14" aria-hidden="true"><rect x="0.5" y="2.5" width="13" height="9" fill="none" stroke="#4b4b4b"/><path d="M.5 2.5L7 8l6.5-5.5" fill="none" stroke="#4b4b4b"/></svg>nim.tressoli@lorantte-example.com</li>
    <li><svg width="14" height="14" viewBox="0 0 14 14" aria-hidden="true"><circle cx="7" cy="7" r="6" fill="none" stroke="#4b4b4b"/><ellipse cx="7" cy="7" rx="2.6" ry="6" fill="none" stroke="#4b4b4b"/><path d="M1 7h12" stroke="#4b4b4b"/></svg>www.lorantte-example.com</li>
    <li class="group-start"><svg width="14" height="14" viewBox="0 0 14 14" aria-hidden="true"><rect x="1" y="1" width="12" height="12" fill="#4b4b4b"/></svg>lorantte_label</li>
    <li><svg width="14" height="14" viewBox="0 0 14 14" aria-hidden="true"><rect x="1" y="1" width="12" height="12" fill="#4b4b4b"/></svg>lorantte</li>
  </ul>
</section>

<section class="card card--back" aria-label="Business card back">
  <div class="back__ornament" role="img" aria-label="Grey floral flourish ornament"></div>
  <div class="back__gloss"></div>
  <div class="back__brand">
    <div class="brand-name">Lorantte</div>
    <div class="brand-suffix">Co., LTD</div>
  </div>
  <div class="back__band">Glamour – Sophistication – Unique</div>
  <div class="back__edge"></div>
</section>

</body>
</html>
```